Copperfox Billboard

Please design a billboard using my photos and logos.
For photo of truck please crop the truck itself out and not have the trees / dirt in photo.
Please put " Best Prices in Sevier County"
Please put " 30-yard Dumpsters Starting at 600.00"
Please put " 16-yard Dumpsters Starting at 300.0"
Please put " Delivery and Pickup 7 Days a week"
Billboard size will be 10 ft tall 30 ft wide

```html
<!DOCTYPE html>
<html lang="en">
<head>
<meta charset="UTF-8">
<title>Copperfox Dumpsters Billboard</title>
<link href="https://fonts.googleapis.com/css2?family=Fira+Sans+Extra+Condensed:wght@600;700&family=Open+Sans:wght@600&display=swap" rel="stylesheet">
<style>
  :root {
    --purple: #561bae;
    --purple-deep: #3b0f88;
    --purple-light: #7a3fd0;
    --teal: #1fb3b3;
    --teal-light: #3fd0cc;
    --yellow: #ffc20e;
    --orange: #f7941d;
    --white: #ffffff;
  }
  * { margin: 0; padding: 0; box-sizing: border-box; }
  html, body { width: 1200px; height: 400px; overflow: hidden; background: var(--purple); }
  .billboard {
    position: relative;
    width: 1200px;
    height: 400px;
    overflow: hidden;
    background: radial-gradient(circle at 20% 30%, var(--purple-light) 0%, var(--purple) 45%, var(--purple) 100%);
  }
  .backdrop { position: absolute; inset: 0; }
  .headline {
    position: absolute;
    left: 57px;
    top: 40px;
    font-family: "Fira Sans Extra Condensed", "Arial Narrow", sans-serif;
    font-weight: 700;
    font-size: 80px;
    line-height: 78px;
    color: var(--white);
    letter-spacing: -0.5px;
    text-shadow: 2px 3px 6px rgba(20, 0, 60, 0.35);
  }
  .headline .accent { color: var(--yellow); }
  .price-list {
    position: absolute;
    left: 56px;
    top: 244px;
    list-style: none;
    font-family: "Open Sans", Arial, sans-serif;
    font-weight: 600;
    font-size: 18.5px;
    color: var(--white);
  }
  .price-list li {
    display: flex;
    align-items: center;
    height: 37px;
  }
  .price-list svg { width: 20px; height: 18px; margin-right: 13px; flex: none; }
  .truck-photo {
    position: absolute;
    left: 487px;
    top: 34px;
    width: 570px;
    height: 334px;
    border-radius: 40px 60px 30px 90px;
    background: linear-gradient(100deg, #f2f2f4 0%, #e4e4e8 45%, #4a2490 70%, #2a1a55 100%);
  }
  .service-badge {
    position: absolute;
    left: 980px;
    top: 42px;
    width: 186px;
    height: 112px;
    border-radius: 50%;
    background: var(--yellow);
    border: 4px solid var(--purple);
    display: flex;
    flex-direction: column;
    align-items: center;
    justify-content: center;
    font-family: "Fira Sans Extra Condensed", "Arial Narrow", sans-serif;
    font-weight: 600;
    color: var(--purple-deep);
    text-align: center;
  }
  .service-badge .badge-small { font-size: 18px; line-height: 20px; }
  .service-badge .badge-large { font-size: 31px; line-height: 34px; }
  .brand-name {
    position: absolute;
    right: 42px;
    top: 322px;
    font-family: "Fira Sans Extra Condensed", "Arial Narrow", sans-serif;
    font-weight: 700;
    font-size: 34px;
    color: var(--white);
    letter-spacing: 0.5px;
  }
</style>
</head>
<body>
  <div class="billboard">
    <svg class="backdrop" width="1200" height="400" viewBox="0 0 1200 400" aria-hidden="true">
      <defs>
        <radialGradient id="tealGlow" cx="0.5" cy="0.4" r="0.6">
          <stop offset="0" stop-color="var(--teal-light)"/>
          <stop offset="1" stop-color="var(--teal)"/>
        </radialGradient>
      </defs>
      <circle cx="866" cy="110" r="323" fill="var(--yellow)"/>
      <circle cx="868" cy="104" r="311" fill="url(#tealGlow)"/>
      <path d="M860 292 L1200 200 L1200 400 L860 400 Z" fill="var(--purple)" opacity="0"/>
    </svg>

    <h1 class="headline">
      <span class="accent">Best Prices</span> in<br>Sevier County
    </h1>

    <ul class="price-list">
      <li>
        <svg viewBox="0 0 20 18" aria-hidden="true">
          <polygon points="6,1 20,9 6,17" fill="var(--orange)"/>
          <polygon points="0,1 12,9 0,17" fill="var(--white)"/>
        </svg>
        30-Yard Dumpsters Starting at 600.00
      </li>
      <li>
        <svg viewBox="0 0 20 18" aria-hidden="true">
          <polygon points="6,1 20,9 6,17" fill="var(--orange)"/>
          <polygon points="0,1 12,9 0,17" fill="var(--white)"/>
        </svg>
        16-yard Dumpsters Starting at 300.0
      </li>
    </ul>

    <div class="truck-photo" role="img" aria-label="Photo of a white roll-off truck carrying a purple dumpster container"></div>

    <div class="service-badge">
      <span class="badge-small">Delivery and Pickup</span>
      <span class="badge-large">7 Days a week</span>
    </div>

    <div class="brand-name">Copperfox Dumpsters</div>
  </div>
</body>
</html>
```